Life Coach for Lawyers Business Card Design

Elegant, original, business card design for life coaching service for associate attorneys who work in big law and struggle with stress, overwhelm, and time management. Double sided design.

Target Market(s)

Women associate attorneys who work in big law and struggle with stress, overwhelm, and time management.

Industry/Entity Type

Life Coaching

Contact Information for Business Card

Marissa Pendrell
Life Coach
518.677.3941
calmbriefcounsel.net
marissa@calmbriefcounsel.net
@calmbriefcounsel (Instagram)

Font styles to use
Other font styles liked:
• Silver South font duo. See uploaded files.

Requirements
Must have
• Icons for phone, website, email, and Instagram instead of words. Specific colors used in my logo (171B2B, 421121, FFFFFF)
Nice to have
• Foil. Embossed. Feminine design.
Should not have
• Any colors other than those used in logo. See uploaded files.

```html
<!DOCTYPE html>
<html lang="en">
<head>
<meta charset="utf-8">
<title>Calm Brief Counsel – Business Card</title>
<link rel="stylesheet" href="https://fonts.googleapis.com/css2?family=Cormorant+Garamond:wght@500&family=Mrs+Saint+Delafield&display=swap">
<style>
  :root {
    --stage: #6d6e71;
    --navy: #171b2b;
    --navy-light: #1e2336;
    --ink: #ffffff;
    --serif: "Cormorant Garamond", serif;
    --script: "Mrs Saint Delafield", cursive;
  }
  html, body {
    margin: 0;
    padding: 0;
    width: 1200px;
    height: 1200px;
    overflow: hidden;
    background: var(--stage);
  }
  .canvas {
    position: relative;
    width: 1200px;
    height: 1200px;
  }
  .card {
    position: absolute;
    left: 110px;
    width: 982px;
    height: 486px;
    background: linear-gradient(155deg, var(--navy-light) 0%, var(--navy) 55%, var(--navy-light) 100%);
    color: var(--ink);
    overflow: hidden;
  }
  .card--front { top: 61px; }
  .card--back { top: 641px; }

  .brand-seal {
    position: absolute;
    border: 1.5px solid var(--ink);
    border-radius: 50%;
    display: flex;
    align-items: center;
    justify-content: center;
    text-align: center;
    font-family: var(--serif);
    font-weight: 500;
    text-transform: uppercase;
    color: var(--ink);
    box-sizing: border-box;
  }
  .brand-seal--large {
    left: 346px;
    top: 99px;
    width: 288px;
    height: 288px;
    font-size: 30px;
    letter-spacing: 5px;
    line-height: 1.35;
  }
  .brand-seal--small {
    left: 116px;
    top: 43px;
    width: 176px;
    height: 176px;
    font-size: 18px;
    letter-spacing: 3px;
    line-height: 1.35;
  }

  .person-name {
    position: absolute;
    left: 580px;
    top: 66px;
    margin: 0;
    font-family: var(--script);
    font-weight: 400;
    font-size: 64px;
    line-height: 1;
    white-space: nowrap;
  }
  .person-role {
    position: absolute;
    left: 580px;
    top: 128px;
    margin: 0;
    font-family: var(--script);
    font-weight: 400;
    font-size: 44px;
    line-height: 1;
    white-space: nowrap;
  }

  .contact-list {
    position: absolute;
    left: 388px;
    top: 232px;
    margin: 0;
    padding: 0;
    list-style: none;
  }
  .contact-item {
    display: flex;
    align-items: center;
    height: 40px;
  }
  .contact-icon {
    width: 44px;
    height: 28px;
    border: 1.5px solid var(--ink);
    border-radius: 14px;
    display: flex;
    align-items: center;
    justify-content: center;
    box-sizing: border-box;
    margin-right: 20px;
    flex-shrink: 0;
  }
  .contact-icon svg { width: 16px; height: 16px; }
  .contact-text {
    font-family: var(--script);
    font-size: 40px;
    line-height: 1;
    white-space: nowrap;
    letter-spacing: 0.5px;
  }
  .contact-text--digits {
    font-size: 26px;
    letter-spacing: 1px;
  }
</style>
</head>
<body>
<main class="canvas">

  <section class="card card--front" aria-label="Card front">
    <div class="brand-seal brand-seal--large">Calm<br>Brief<br>Counsel</div>
  </section>

  <section class="card card--back" aria-label="Card back">
    <div class="brand-seal brand-seal--small">Calm<br>Brief<br>Counsel</div>

    <h1 class="person-name">Marissa Pendrell</h1>
    <p class="person-role">Life Coach</p>

    <ul class="contact-list">
      <li class="contact-item">
        <span class="contact-icon" aria-label="Phone">
          <svg viewBox="0 0 24 24" fill="none" stroke="#ffffff" stroke-width="2" stroke-linecap="round" stroke-linejoin="round">
            <path d="M5 3h4l2 5-2.5 1.5a11 11 0 0 0 6 6L16 13l5 2v4a2 2 0 0 1-2 2A16 16 0 0 1 3 5a2 2 0 0 1 2-2z"/>
          </svg>
        </span>
        <span class="contact-text contact-text--digits">518.677.3941</span>
      </li>
      <li class="contact-item">
        <span class="contact-icon" aria-label="Email">
          <svg viewBox="0 0 24 24" fill="none" stroke="#ffffff" stroke-width="2.2" stroke-linecap="round">
            <circle cx="12" cy="12" r="4"/>
            <path d="M16 8v5.5a2.5 2.5 0 0 0 5 0V12a9 9 0 1 0-3.5 7.1"/>
          </svg>
        </span>
        <span class="contact-text">marissa@calmbriefcounsel.net</span>
      </li>
      <li class="contact-item">
        <span class="contact-icon" aria-label="Social handle"></span>
        <span class="contact-text">@calmbriefcounsel</span>
      </li>
      <li class="contact-item">
        <span class="contact-icon" aria-label="Website">
          <svg viewBox="0 0 24 24" fill="none" stroke="#ffffff" stroke-width="1.8">
            <circle cx="12" cy="12" r="9"/>
            <ellipse cx="12" cy="12" rx="4" ry="9"/>
            <path d="M3 12h18M5 7h14M5 17h14"/>
          </svg>
        </span>
        <span class="contact-text">calmbriefcounsel.net</span>
      </li>
    </ul>
  </section>

</main>
</body>
</html>
```